New Bottle Label for our Velmoris Grand Reserva Brandy

Graphic Design Brief
We need a new bottle label for our Brandy Gran Reserva that we want to bring to the market.
Please have a look at all our current bottles and labels and the feel of our company under www.velmoris-distill.ch. We would like the design to be still different to the rest - as it is not a whisky, not a fruit product, not a spirit like a gin, thus we need to create like a new family, but still fitting in with the rest of the products.
The bottle that we will be using for the brand is a different one than the one that we already have, the design of the bottle is attached with a document.
I have also attached a briefing in regards to Brandy in general for your information.
### 1. What is Brandy?
Brandy is a distilled spirit made from fermented wine or other fruit wines. It is traditionally aged in oak barrels, which gives it its characteristic color and rich flavor. The aging process in oak is essential for developing the aromas and quality of the brandy.
### 2. What is Brandy Reserva?
A Brandy labeled as "Reserva" has undergone a longer aging process, typically at least 2 to 3 years, in oak barrels. This aging gives the brandy a deeper, more complex flavor profile and a darker color. "Reserva" is often an indication of higher quality.
### 3. Who enjoys drinking Brandy?
Brandy is typically favored by those who appreciate a deep, rich tasting experience. This often includes older consumers who value the time-aged complexity of the spirit. However, Brandy is also gaining popularity among younger people, especially through cocktails and modern serving styles.
### 4. Why is Brandy trending?
Brandy is experiencing a resurgence as consumers increasingly value quality and artisanal production methods. Its versatility in cocktails and association with traditional, luxurious experiences have also contributed to its renewed popularity.
### 5. What colors would be associated with Brandy?
The typical colors associated with Brandy are warm gold, amber, and deep golden-brown tones. These colors reflect the aging process in oak barrels and the richness of the flavors. Other associated colors might include dark brown and mahogany.
### 6. What is important to customers when buying Brandy?
Customers care about the origin of the Brandy, the aging time, the quality of the ingredients, the production method, and the brand. They also pay attention to the prestige of the product and the authenticity of the production.
### 7. What is not important to customers when buying Brandy?
For many customers, the price and packaging (unless it’s especially exclusive) may be less important than the quality and taste of the Brandy. The distillery name might be less significant if it isn’t tied to a particular reputation.
### 8. What do customers know about Swiss Brandy?
Swiss Brandy is still relatively unknown in many markets, but customers who are familiar with it appreciate the precision and quality of Swiss production. Swiss Brandy is assumed to be made with care and under strict quality standards.
### 9. What is Brandy Gran Reserva?
**Brandy Gran Reserva** is an even higher quality and longer-aged version of Brandy. Generally, a Gran Reserva is aged for at least 5 to 10 years or more in oak barrels. This extended aging process gives the Brandy an especially deep, complex flavor profile and often a darker, richer color. Gran Reserva is often regarded as the top-tier product within a Brandy range and appeals to discerning consumers who value quality, refinement, and a luxurious tasting experience.
The label “Gran Reserva” thus indicates the highest quality level for Brandies, similar to other spirits (like wine or whisky), where the aging time is a critical factor.
We age our Brandy Gran Reserva in the Solara way.
### 10. What emotions are associated with Brandy?
Brandy is often associated with luxury, relaxation, and comfort. It evokes feelings of tradition, elegance, and sophistication. Drinking Brandy is frequently seen as a moment of reflection and enjoyment.
### 11. How should Brandy be marketed?
Brandy should be marketed with a focus on its artisanal production, quality, and tradition. A narrative around the product, its aging, and origin can help create an emotional connection with the customer. The marketing should also emphasize the versatility of Brandy, whether consumed neat or in cocktails.
**Label design**:
The label should reflect the exclusivity of the product, with an elegant, minimalist design. The label should include information about the aging time, the use of oak barrels, and a brief story about the Brandy’s production.
we would like to have a modern look to the whole deisgn of the brandy
Customers that like Brandy
Switzerland
Distillery

```html
<!DOCTYPE html>
<html lang="en">
<head>
<meta charset="utf-8">
<title>Velmoris Brandy Gran Reserva – Label</title>
<link rel="stylesheet" href="https://fonts.googleapis.com/css2?family=Fraunces:opsz,wght@9..144,300;9..144,400;9..144,600&family=Roboto+Slab:wght@500;600;700&family=Pinyon+Script&family=Barlow+Condensed:wght@600&family=DM+Sans:wght@400&display=swap">
<style>
  :root {
    --page: #ffffff;
    --label: #4b3238;
    --label-deep: #3f2a30;
    --cream: #dcc6a6;
    --cream-soft: #cbb596;
    --white: #fbf7f1;
    --numeral: #5a3f45;
  }
  html, body {
    margin: 0;
    width: 1200px;
    height: 1200px;
    overflow: hidden;
    background: var(--page);
  }
  .label {
    position: absolute;
    left: 300px;
    top: 55px;
    width: 600px;
    height: 1090px;
    color: var(--cream);
    text-align: center;
  }
  .label__shape { position: absolute; inset: 0; }
  .label__row {
    position: absolute;
    left: 0;
    right: 0;
    margin: 0;
    line-height: 1;
  }
  .since {
    top: 82px;
    font: 400 19px "Fraunces", serif;
    letter-spacing: 2px;
  }
  .brand-name {
    top: 196px;
    font: 700 74px "Roboto Slab", serif;
    letter-spacing: 1px;
  }
  .brand-sub {
    top: 268px;
    font: 600 33px/38px "Roboto Slab", serif;
    letter-spacing: 2px;
  }
  .age-numeral {
    top: 395px;
    font: 600 300px "Fraunces", serif;
    color: var(--numeral);
    letter-spacing: -10px;
  }
  .selection {
    top: 424px;
    font: 600 23px "Barlow Condensed", sans-serif;
    letter-spacing: 0.5px;
  }
  .product {
    top: 480px;
    font: 600 96px "Fraunces", serif;
    color: var(--white);
    letter-spacing: 2px;
  }
  .reserve {
    top: 590px;
    font: 400 38px "Pinyon Script", cursive;
    color: var(--cream-soft);
  }
  .divider-v {
    position: absolute;
    left: 299px;
    top: 648px;
    width: 2px;
    height: 44px;
    background: var(--cream);
  }
  .aging {
    top: 716px;
    font: 300 28px "Fraunces", serif;
    letter-spacing: 0.5px;
  }
  .aging b { font-weight: 600; font-size: 32px; }
  .aging .sep { margin: 0 10px; font-weight: 300; }
  .rule {
    position: absolute;
    height: 2px;
    background: var(--cream);
  }
  .rule--short { left: 190px; width: 220px; top: 768px; }
  .rule--wide { left: 66px; width: 468px; top: 1010px; }
  .oak {
    top: 780px;
    font: 600 28px "Fraunces", serif;
    letter-spacing: 0.5px;
  }
  .dots {
    top: 846px;
    font: 400 22px "DM Sans", sans-serif;
    letter-spacing: 6px;
  }
  .story {
    top: 884px;
    left: 95px;
    right: 95px;
    font: 400 15.5px/22px "DM Sans", sans-serif;
    color: var(--cream-soft);
  }
  .facts {
    top: 1020px;
    left: 66px;
    right: 66px;
    font: 300 25px "Fraunces", serif;
    display: flex;
    justify-content: space-between;
  }
</style>
</head>
<body>
  <main class="label">
    <svg class="label__shape" width="600" height="1090" viewBox="0 0 600 1090" aria-hidden="true">
      <path d="M0 70 Q300 -30 600 70 L600 1090 L0 1090 Z" fill="var(--label)"/>
      <path d="M22 86 Q300 -6 578 86 L578 1066 L22 1066 Z" fill="none" stroke="var(--cream)" stroke-width="4"/>
      <path d="M44 100 Q300 10 556 100 L556 1044 L44 1044 Z" fill="var(--label-deep)" opacity="0.25"/>
      <path id="arc-line" d="M90 96 Q300 24 510 96" fill="none"/>
      <text font-family="Roboto Slab, serif" font-weight="600" font-size="22" letter-spacing="3" fill="var(--cream)" text-anchor="middle">
        <textPath href="#arc-line" startOffset="50%">VELMORIS SWISS DISTILLERY</textPath>
      </text>
    </svg>

    <p class="label__row since">SINCE 2007</p>
    <p class="label__row brand-name">Velmoris</p>
    <p class="label__row brand-sub">SWISS<br>DISTILLERY</p>

    <p class="label__row age-numeral" aria-hidden="true">10</p>
    <p class="label__row selection">· FNEST SELECTION ·</p>
    <h1 class="label__row product">BRANDY</h1>
    <p class="label__row reserve">Solara Gran Reserva</p>
    <span class="divider-v"></span>

    <p class="label__row aging">AGING<span class="sep">|</span><b>10</b><span class="sep">|</span>YEARS</p>
    <span class="rule rule--short"></span>
    <p class="label__row oak">OAK BARRELS</p>
    <p class="label__row dots">• • •</p>
    <p class="label__row story">Lorem ipsum dolor sit amet, consectetuer adipiscing elit, sed diam nonummy nibh euismod tincidunt ut laoreet dolore magna aliquam erat volutpat. Ut wisi enim ad minim veniam, quis nostrud exerci tation ullamcorpe</p>

    <span class="rule rule--wide"></span>
    <p class="label__row facts"><span>700ML</span><span>|</span><span>SWISS MADE</span><span>|</span><span>40% VOL</span></p>
  </main>
</body>
</html>
```